6' Banner Stands for exhibiting to Health Fairs with an audience of age 55+

We need designs for two 6' banner stands to stand on either side of our exhibition tables. We offer Hereditary Cancer Screening. I want the banners to have the same look and feel as the logo and the files color scheme logo, etc..

The Banners should have "Hereditary Cancer Screening" at the top with the Tag Line "The Test You Take For Them" underneath. A photo of grandparents with kids/grandkids and underneath the photos in large font one of the following messages:
1) "A Simple Swab Could Save A Family Members LIFE Get Tested Today!"
2) "Does Cancer Run In Your Family? Get Tested Today!"
3) "Knowledge Is Power" "Get Tested Today!"
4) "Will You Give Your Loved Ones The Information To Beat Cancer In Their Lives? Get Tested Today!
5) Knowledge Is Power Get Tested Today!"
Updates

Thank you all for your designs I now have the exact specs for the banners, so please use these as you update your designs. 31.5 inches X 83.25 inches and add a 1/2 inch bleed to all 4 sides. Thank you.

Target Market(s)

Persons 55+ who are grandparents

Industry/Entity Type

Healthcare

Font styles to use
Sans Serif
Other font styles liked:
• Comic Sans for "The Test You Take For Them"

Colors
9bcb3c
0356a4
ffffff

Requirements
Must have
• the main focus should be the hereditary cancer screening; "Hereditary Cancer Screening";
• "The test you order for them" in Comic Sans font underneath
• A photo or photos of grandparents with their grandchildren (multiple ethnicities)
• One of the slogans listed above
• GET TESTED TODAY underneath the messages at the bottom of the banner highlighted and eye catching
• www.kinhealthcheckup.net
Nice to have
• Logo at the top or bottom

```html
<!DOCTYPE html>
<html lang="en">
<head>
<meta charset="utf-8">
<title>Hereditary Cancer Screening – Banner Stand</title>
<link href="https://fonts.googleapis.com/css2?family=Montserrat:wght@400;500;700;800&family=Comic+Neue:wght@700&display=swap" rel="stylesheet">
<style>
  :root{
    --brand-green:#9bcb3c;
    --brand-blue:#0356a4;
    --white:#ffffff;
    --stage:#6e6e6e;
    --photo-warm-1:#e9e3dc;
    --photo-warm-2:#cfd8e0;
    --photo-beach-1:#9fc6e6;
    --photo-beach-2:#d9cdb8;
  }
  html,body{margin:0;padding:0;}
  body{
    width:1200px;height:2419px;overflow:hidden;
    background:var(--stage);
    font-family:'Montserrat',Arial,sans-serif;
  }
  .banner{
    position:absolute;left:215px;top:60px;
    width:447px;height:1335px;
    transform:scale(1.7228);transform-origin:top left;
    background:var(--white);overflow:hidden;
  }
  .banner-shapes{position:absolute;inset:0;width:447px;height:1335px;}
  .line{position:absolute;left:0;right:0;text-align:center;white-space:nowrap;}
  .brand{
    position:absolute;left:120px;top:427px;display:flex;align-items:center;gap:12px;
  }
  .brand-mark{width:62px;height:62px;border-radius:50%;background:var(--brand-blue);}
  .brand-name{
    color:var(--brand-blue);font-weight:700;font-size:19px;line-height:21px;letter-spacing:.5px;
  }
  .title-small{top:519px;font-size:29px;line-height:38px;font-weight:800;color:var(--brand-blue);letter-spacing:.3px;}
  .title-large{top:556px;font-size:54px;line-height:64px;font-weight:800;color:var(--brand-blue);letter-spacing:.5px;}
  .tagline{top:627px;height:30px;font-family:'Comic Neue','Comic Sans MS',cursive;font-weight:700;font-size:21px;line-height:30px;color:var(--white);letter-spacing:.8px;}
  .msg-question{top:1013px;font-size:28px;line-height:44px;font-weight:800;color:var(--white);}
  .msg-family{top:1068px;font-size:45px;line-height:54px;font-weight:500;color:var(--brand-green);}
  .msg-swab{top:1129px;font-size:21px;line-height:38px;font-weight:800;color:var(--white);}
  .msg-life{top:1178px;font-size:26px;line-height:36px;font-weight:500;color:var(--brand-blue);}
  .call-to-action{top:1274px;font-size:17px;line-height:22px;font-weight:800;color:var(--brand-green);letter-spacing:.4px;}
  .web-address{top:1303px;font-size:11px;line-height:15px;font-weight:500;color:var(--white);}
</style>
</head>
<body>
  <div class="banner">
    <svg class="banner-shapes" viewBox="0 0 447 1335" xmlns="http://www.w3.org/2000/svg">
      <defs>
        <linearGradient id="warm" x1="0" y1="0" x2="1" y2="1">
          <stop offset="0" stop-color="var(--photo-warm-1)"/>
          <stop offset="1" stop-color="var(--photo-warm-2)"/>
        </linearGradient>
        <linearGradient id="beach" x1="0" y1="0" x2="0" y2="1">
          <stop offset="0" stop-color="var(--photo-beach-1)"/>
          <stop offset="0.55" stop-color="#b9d3e3"/>
          <stop offset="1" stop-color="var(--photo-beach-2)"/>
        </linearGradient>
      </defs>
      <rect x="0" y="0" width="447" height="400" fill="url(#warm)" role="img" aria-label="Photo of a smiling grandmother hugging her young granddaughter"/>
      <polygon points="0,352 224,243 447,352 447,620 0,620" fill="var(--brand-blue)"/>
      <polygon points="0,383 224,280 447,383 447,620 0,620" fill="var(--white)"/>
      <polygon points="0,395 224,292 447,395 447,620 0,620" fill="var(--brand-green)"/>
      <polygon points="0,480 224,365 447,480 447,620 0,620" fill="var(--white)"/>
      <rect x="0" y="627" width="447" height="30" fill="var(--brand-green)"/>
      <rect x="0" y="675" width="447" height="5" fill="var(--brand-blue)"/>
      <rect x="0" y="685" width="447" height="300" fill="url(#beach)" role="img" aria-label="Photo of grandparents walking on the beach with their grandchildren"/>
      <rect x="0" y="990" width="447" height="5" fill="var(--brand-blue)"/>
      <rect x="0" y="1013" width="447" height="44" fill="var(--brand-green)"/>
      <rect x="0" y="1129" width="447" height="38" fill="var(--brand-blue)"/>
      <polyline points="58,1304 224,1216 390,1304" fill="none" stroke="var(--brand-green)" stroke-width="9"/>
      <polygon points="24,1328 224,1232 424,1328" fill="var(--brand-blue)"/>
      <rect x="0" y="1328" width="447" height="7" fill="var(--brand-green)"/>
    </svg>

    <div class="brand">
      <div class="brand-mark"></div>
      <div class="brand-name">KINLINE<br>HEALTH<br>GROUP</div>
    </div>

    <div class="line title-small">HEREDITARY CANCER</div>
    <div class="line title-large">SCREENING</div>
    <div class="line tagline">THE TEST YOU TAKE FOR THEM</div>

    <div class="line msg-question">DOES CANCER RUN IN</div>
    <div class="line msg-family">YOUR FAMILY?</div>
    <div class="line msg-swab">A SIMPLE SWAB COULD SAVE</div>
    <div class="line msg-life">A FAMILY MEMBERS LIFE</div>
    <div class="line call-to-action">GET TESTED TODAY!</div>
    <div class="line web-address">www.kinhealthcheckup.net</div>
  </div>
</body>
</html>
```